Dravolith Business Card

I have a logo that I would like to use to design the Business Card for Dravolith Construction LLC. We are a commercial general contractor in Harlow Bend Texas. Id like a simple and sleek design. Message me if you have any questions. Thanks

Industry/Entity Type

Contractor

```html
<!DOCTYPE html>
<html lang="en">
<head>
<meta charset="utf-8">
<title>Dravolith Business Card</title>
<link rel="stylesheet" href="https://fonts.googleapis.com/css2?family=Share+Tech+Mono&display=swap">
<style>
  :root {
    --backdrop: #ececec;
    --silver-dark: #c4c7cc;
    --silver-light: #eceded;
    --info-bg: #ebebeb;
    --charcoal: #464444;
    --brand-blue: #3d71ae;
    --text-blue: #4a74b0;
    --ink: #2f2f31;
  }
  * { box-sizing: border-box; margin: 0; padding: 0; }
  html, body {
    width: 1200px; height: 782px; overflow: hidden;
    background: var(--backdrop);
    font-family: "Share Tech Mono", monospace;
  }
  .stage { position: relative; width: 1200px; height: 782px; }

  .card {
    position: absolute;
    display: flex; flex-direction: column;
    overflow: hidden;
    box-shadow: 0 2px 8px rgba(0,0,0,0.18);
  }
  .card--front { left: 245px; top: 108px; width: 312px; height: 555px; }
  .card--back  { left: 709px; top: 84px;  width: 327px; height: 571px; }

  .card__brand {
    background: linear-gradient(112deg,
      var(--silver-dark) 0%, #d6d8db 22%, var(--silver-light) 42%,
      #cbcdd1 55%, #e2e3e5 72%, var(--silver-dark) 100%);
    display: flex; flex-direction: column; align-items: center; justify-content: center;
    gap: 10px;
    border-bottom: 3px solid var(--brand-blue);
  }
  .card--front .card__brand { height: 283px; }
  .card--back  .card__brand { height: 306px; }

  .brand-mark { width: 22px; height: 22px; background: var(--brand-blue); }
  .card--back .brand-mark { width: 30px; height: 30px; }

  .brand-name {
    color: var(--ink);
    text-align: center;
    font-size: 15px; line-height: 1.15; letter-spacing: 0.5px;
    text-transform: uppercase;
  }
  .card--back .brand-name { font-size: 21px; }

  .contact {
    background: var(--info-bg);
    height: 131px;
    list-style: none;
    padding: 4px 0 0 28px;
  }
  .contact__item {
    display: flex; align-items: center;
    height: 31px;
    color: var(--text-blue);
    font-size: 16px; letter-spacing: 2.4px;
    white-space: nowrap;
  }
  .contact__icon { width: 20px; height: 20px; margin-right: 22px; flex: none; }

  .band-charcoal { background: var(--charcoal); height: 50px; }
  .band-blue { background: var(--brand-blue); flex: 1; }

  .band-sheen {
    height: 84px;
    background: linear-gradient(180deg, #f3f3f3 0%, #e9e9e9 35%, #bdbdbd 70%, #dadada 100%);
    border-bottom: 4px solid var(--brand-blue);
  }
  .card--back .band-charcoal { height: 52px; }
</style>
</head>
<body>
<main class="stage">

  <section class="card card--front" aria-label="Business card front">
    <header class="card__brand">
      <span class="brand-mark" aria-hidden="true"></span>
      <p class="brand-name">Dravolith<br>Construction LLC</p>
    </header>
    <ul class="contact">
      <li class="contact__item">
        <svg class="contact__icon" viewBox="0 0 20 20" fill="none" stroke="var(--text-blue)" stroke-width="1.5">
          <path d="M10 18 C6 13 4.5 10.5 4.5 7.5 A5.5 5.5 0 0 1 15.5 7.5 C15.5 10.5 14 13 10 18 Z"/>
          <circle cx="10" cy="7.5" r="2"/>
        </svg>
        Harlow Bend Texas
      </li>
      <li class="contact__item">
        <svg class="contact__icon" viewBox="0 0 20 20" fill="none" stroke="var(--text-blue)" stroke-width="1.5">
          <rect x="1.5" y="4.5" width="17" height="11"/>
          <path d="M1.5 4.5 L10 11 L18.5 4.5"/>
        </svg>
        your_mail@mail.com
      </li>
      <li class="contact__item">
        <svg class="contact__icon" viewBox="0 0 20 20" fill="none" stroke="var(--text-blue)" stroke-width="1.5">
          <rect x="5.5" y="1.5" width="9" height="17" rx="1.5"/>
          <line x1="5.5" y1="15" x2="14.5" y2="15"/>
        </svg>
        xxx xxxx xxx
      </li>
      <li class="contact__item">
        <svg class="contact__icon" viewBox="0 0 20 20" fill="none" stroke="var(--text-blue)" stroke-width="1.5">
          <rect x="1.5" y="3" width="17" height="11"/>
          <path d="M8 14 L7 17.5 M12 14 L13 17.5 M5.5 17.5 H14.5"/>
        </svg>
        www.yoursite.com
      </li>
    </ul>
    <div class="band-charcoal"></div>
    <div class="band-blue"></div>
  </section>

  <section class="card card--back" aria-label="Business card back">
    <header class="card__brand">
      <span class="brand-mark" aria-hidden="true"></span>
      <p class="brand-name">Dravolith<br>Construction LLC</p>
    </header>
    <div class="band-sheen"></div>
    <div class="band-charcoal"></div>
    <div class="band-blue"></div>
  </section>

</main>
</body>
</html>
```